AMAZING WEBSITE DESIGN NEEDED FOR MAID / CLEANING SERVICE

NOTE: This is Website Design Only - No coding required

Please submit your designs ASAP as we want to pick a winner and get started!

Hey,

We are looking for a new amazing website design for a maid or cleaning service.

They have a horrible website that we want turned into a masterpiece.

As you will see on their current site:

http://tidyhavenco.examplehost.net/

They have a lot of stuff, very disorganized, and need help.

Here is what we need:

Colors: Same as current site, Orange, Gray, Black

Menu: Horizontal with same Menu items

Need a spot for a video on the homepage

Want content to be structured in a great format that is easy to read.

Want to highlight commercial and residential on the website homepage.

Also want a spot for customer testimonials

We want the site clean, professional, fresh and modern.

Please help by matching the logo design.

I look forward to your designs!
Updates

Hi All! Really appreciate your efforts and designs. I will be meeting with our client on Monday and will then be able to provide feedback after our meeting. If you have other ideas, please submit them. The more I can show him the better! Thanks!

Target Market(s)

The target market is residential home owners as well as commercial businesses who need cleaning on a regular basis.

This company cleans homes and offices for individuals.

Industry/Entity Type

Residential

Font styles to use
Sans Serif

Requirements
Must have
• Must match logo colors
Must have spot for video
Must have a clean look
Must have a bold look
Nice to have
• Highly visual
Should not have
• clutter
messy design
hard to read

```html
<!DOCTYPE html>
<html lang="en">
<head>
<meta charset="utf-8">
<title>Tidy Haven Co – Home</title>
<link href="https://fonts.googleapis.com/css2?family=Open+Sans:ital,wght@0,300;0,400;0,600;0,700;1,400&family=Raleway:wght@300;700&display=swap" rel="stylesheet">
<style>
:root{
  --orange:#ef7a16;
  --grey:#777777;
  --dark:#333333;
  --text:#666666;
  --light:#f3f3f3;
  --footer:#5b5b5b;
  --footer-dark:#454545;
  --white:#ffffff;
}
*{margin:0;padding:0;box-sizing:border-box}
html,body{width:797px;height:1200px;overflow:hidden;background:var(--white);font-family:"Open Sans",sans-serif;color:var(--text)}
.page{position:relative;width:797px;height:1200px}
.topbar{position:absolute;top:0;left:0;width:797px;height:4px;background:var(--orange)}
.header{position:absolute;top:4px;left:0;width:797px;height:95px;border-bottom:1px solid #e2e2e2}
.brand{position:absolute;left:86px;top:34px;display:flex;align-items:center;gap:8px}
.brand-mark{width:20px;height:20px;background:var(--orange)}
.brand-name{font-size:24px;font-weight:700;color:var(--orange);letter-spacing:-.3px}
.brand-tag{position:absolute;left:114px;top:74px;font-size:8px;font-style:italic;color:var(--grey);font-weight:600}
.nav{position:absolute;left:299px;top:0;height:95px;display:flex;align-items:center;font-size:10px;color:var(--dark)}
.nav a{display:flex;align-items:center;height:95px;padding:0 8px;text-decoration:none;color:var(--dark)}
.nav a.active{background:var(--orange);color:var(--white);padding:0 11px;margin-right:2px}
.hero{position:absolute;left:73px;top:99px;width:651px;height:284px;background:linear-gradient(100deg,#f4f4f2 0%,#ece7e0 45%,#c69a6a 80%,#9c6a3e 100%)}
.hero-title{position:absolute;left:13px;top:106px;font-family:"Raleway",sans-serif;font-weight:300;font-size:23px;line-height:29px;color:#555}
.hero-title b{font-weight:700}
.welcome{position:absolute;left:73px;top:402px;width:651px;height:116px;background:var(--grey)}
.welcome-photo{position:absolute;left:24px;top:17px;width:84px;height:74px;background:linear-gradient(135deg,#e8a0b8,#f2e6d2 60%,#b9c98a)}
.welcome h1{position:absolute;left:128px;top:14px;font-size:19px;font-weight:400;color:var(--white)}
.welcome h1 b{font-weight:700}
.welcome p{position:absolute;left:128px;top:46px;width:505px;font-size:10px;line-height:16px;color:var(--white)}
.welcome-rule{position:absolute;left:73px;top:518px;width:651px;height:4px;background:#111}
.welcome-pointer{position:absolute;left:386px;top:521px}
.services{position:absolute;top:568px;left:73px;width:651px}
.service{position:absolute;width:186px;text-align:center}
.service svg{display:block;margin:0 auto}
.service h2{margin-top:21px;font-size:12px;font-weight:700;color:var(--orange)}
.service p{margin-top:14px;font-size:9.5px;line-height:14.5px;color:var(--text)}
.service a{display:block;margin-top:19px;font-size:9px;font-style:italic;color:var(--orange);text-decoration:none}
.band{position:absolute;top:770px;left:0;width:797px;height:240px;background:var(--light)}
.band h3{position:absolute;top:14px;font-size:17px;font-weight:300;color:var(--dark)}
.quote{position:absolute;left:76px;width:310px;height:70px}
.avatar{position:absolute;left:0;top:0;width:58px;height:58px;border-radius:50%;background:radial-gradient(circle,#f3e1b0,#e9e9e9 70%)}
.quote p{position:absolute;left:74px;top:2px;width:240px;font-size:9.5px;line-height:12.7px;color:#888}
.quote cite{position:absolute;right:0;top:59px;font-size:9.5px;font-style:normal;color:var(--orange)}
.video{position:absolute;left:430px;top:60px;width:295px;height:155px;background:linear-gradient(120deg,#d9cfc4,#f1eee9 50%,#c9b9a8)}
.video-play{position:absolute;left:129px;top:58px;width:36px;height:30px;background:rgba(30,30,30,.85);border-radius:3px}
.video-bar{position:absolute;left:0;bottom:0;width:295px;height:22px;background:rgba(20,20,20,.75)}
.video-track{position:absolute;left:46px;top:9px;width:180px;height:4px;background:#777}
.video-track span{display:block;width:50px;height:4px;background:#1aa9e0}
.footer{position:absolute;top:1010px;left:0;width:797px;height:160px;background:var(--footer);color:var(--white)}
.footer .col-rule{position:absolute;top:16px;width:1px;height:120px;background:#777}
.footer-brand{position:absolute;left:90px;top:27px;display:flex;align-items:center;gap:6px}
.footer-brand i{width:12px;height:12px;background:var(--white)}
.footer-brand span{font-size:14px;font-weight:700;color:var(--white)}
.footer-about{position:absolute;left:87px;top:60px;width:160px;font-size:8px;line-height:16.8px;font-weight:600}
.footer h4{position:absolute;top:28px;font-size:11.5px;font-weight:700;letter-spacing:.3px}
.socials{position:absolute;left:325px;top:50px;display:flex;gap:6px}
.socials span{width:22px;height:22px;border-radius:50%;background:var(--white);display:flex;align-items:center;justify-content:center}
.newsletter-label{position:absolute;left:325px;top:90px;font-size:9.5px}
.newsletter{position:absolute;left:325px;top:105px;display:flex}
.newsletter input{width:118px;height:22px;border:0;padding:0 8px;font:8px "Open Sans",sans-serif;color:#222}
.newsletter button{width:22px;height:22px;border:0;background:#222;color:var(--white);font:9px "Open Sans",sans-serif}
.contact{position:absolute;left:528px;top:48px;font-size:8px;line-height:12px}
.contact dt{position:absolute;left:0}
.contact dd{margin-left:48px;margin-bottom:2.5px;width:136px;position:relative}
.contact dd::before{content:":";position:absolute;left:-11px}
.copyright{position:absolute;top:1170px;left:0;width:797px;height:30px;background:var(--footer-dark);color:var(--white);font-size:8px;text-align:center;line-height:30px}
</style>
</head>
<body>
<div class="page">
  <div class="topbar"></div>
  <header class="header">
    <div class="brand"><span class="brand-mark"></span><span class="brand-name">Tidy Haven Co</span></div>
    <div class="brand-tag">Quality Commercial &amp; Residential Cleaning</div>
    <nav class="nav">
      <a class="active" href="#">Home</a>
      <a href="#">Our Services</a>
      <a href="#">Why Us</a>
      <a href="#">Testimonials</a>
      <a href="#">Special Offers</a>
      <a href="#">About Us</a>
      <a href="#">Contact Us</a>
    </nav>
  </header>

  <section class="hero" role="img" aria-label="Smiling woman wiping a wooden table with a yellow cloth in a bright living room">
    <h2 class="hero-title">You Do The <b>Relaxing</b><br>Let Us Do The <b>Cleaning</b></h2>
  </section>

  <section class="welcome">
    <div class="welcome-photo" role="img" aria-label="Woman arranging jars on white shelves"></div>
    <h1>Welcome To <b>TIDY HAVEN CO</b></h1>
    <p>Lorem ipsum dolor sit amet, consectetuer adipiscing elit, sed diam nonummy nibh euismod tincidunt ut laoreet dolore magna aliquam erat volutpat. Ut wisi enim ad minim veniam, quis nostrud exerci tation ullamcorper suscipit lobortis nisl ut aliquip ex ea commodo consequat.</p>
  </section>
  <div class="welcome-rule"></div>
  <svg class="welcome-pointer" width="20" height="17" viewBox="0 0 20 17"><path d="M0 0H20L10 17Z" fill="#111"/></svg>

  <section class="services">
    <div class="service" style="left:0">
      <svg width="48" height="52" viewBox="0 0 48 52" fill="#444"><path d="M2 6L30 0V52H2Z"/><path d="M30 18H47V52H30Z"/><g fill="#fff"><rect x="8" y="10" width="5" height="6"/><rect x="19" y="10" width="5" height="6"/><rect x="8" y="22" width="5" height="6"/><rect x="19" y="22" width="5" height="6"/><rect x="8" y="34" width="5" height="6"/><rect x="19" y="34" width="5" height="6"/><rect x="35" y="26" width="4" height="5"/><rect x="35" y="36" width="4" height="5"/><rect x="13" y="44" width="6" height="8"/></g></svg>
      <h2>Residential</h2>
      <p>Lorem ipsum dolor sit amet, consectetuer adipiscing elit, sed diam nonummy nibh aliquam erat volutpat.</p>
      <a href="#">Learn More</a>
    </div>
    <div class="service" style="left:236px">
      <svg width="48" height="50" viewBox="0 0 48 50" fill="#444"><path d="M2 6H32V48H2Z"/><path d="M32 10Q46 10 46 24V48H32Z"/><rect x="0" y="47" width="48" height="3"/><g fill="#fff"><rect x="6" y="11" width="5" height="5"/><rect x="14" y="11" width="5" height="5"/><rect x="22" y="11" width="5" height="5"/><rect x="6" y="20" width="5" height="5"/><rect x="14" y="20" width="5" height="5"/><rect x="22" y="20" width="5" height="5"/><rect x="6" y="29" width="5" height="5"/><rect x="14" y="29" width="5" height="5"/><rect x="22" y="29" width="5" height="5"/><rect x="6" y="38" width="5" height="5"/><rect x="14" y="38" width="5" height="5"/><rect x="22" y="38" width="5" height="5"/><rect x="36" y="20" width="6" height="2"/><rect x="36" y="27" width="6" height="2"/><rect x="36" y="34" width="6" height="2"/></g></svg>
      <h2>Commercial</h2>
      <p>Lorem ipsum dolor sit amet, consectetuer adipiscing elit, sed diam nonummy nibh aliquam erat volutpat.</p>
      <a href="#">Learn More</a>
    </div>
    <div class="service" style="left:466px">
      <svg width="24" height="54" viewBox="0 0 24 54"><ellipse cx="12" cy="12" rx="9" ry="11" fill="#444"/><path d="M10 23H14L12 26Z" fill="#444"/><path d="M12 26C8 34 16 40 11 53" stroke="#444" stroke-width="1.2" fill="none"/></svg>
      <h2>Special Event</h2>
      <p>Lorem ipsum dolor sit amet, consectetuer adipiscing elit, sed diam nonummy nibh aliquam erat volutpat.</p>
      <a href="#">Learn More</a>
    </div>
  </section>

  <section class="band">
    <h3 style="left:73px">Testimonials</h3>
    <h3 style="left:430px">Featured Video</h3>
    <div class="quote" style="top:62px">
      <div class="avatar" role="img" aria-label="Cleaner holding supplies"></div>
      <p>Brightline Supply provides pre-eminent customer service and I would recommend them to any progressive companies seeking a robust, reliable and state-of-the-art solution.</p>
      <cite>Lorem Ipsum</cite>
    </div>
    <div class="quote" style="top:150px">
      <div class="avatar" role="img" aria-label="Cleaner holding supplies"></div>
      <p>Brightline Supply provides pre-eminent customer service and I would recommend them to any progressive companies seeking a robust, reliable and state-of-the-art solution.</p>
      <cite>Lorem Ipsum</cite>
    </div>
    <div class="video" role="img" aria-label="Video still of a woman mopping a living room floor">
      <div class="video-play"><svg width="36" height="30" viewBox="0 0 36 30"><path d="M14 8L25 15L14 22Z" fill="#fff"/></svg></div>
      <div class="video-bar"><svg width="22" height="22" viewBox="0 0 22 22" style="position:absolute;left:10px"><path d="M8 6L16 11L8 16Z" fill="#fff"/></svg><div class="video-track"><span></span></div></div>
    </div>
  </section>

  <footer class="footer">
    <div class="footer-brand"><i></i><span>Tidy Haven Co</span></div>
    <p class="footer-about">Lorem ipsum dolor sit amet, consecte-tuer adipiscing elit, sed diam nonummy nibh euismod tincidunt ut laoreet dolore magna aliquam erat volutpat.</p>
    <div class="col-rule" style="left:292px"></div>
    <h4 style="left:325px">GET IN TOUCH</h4>
    <div class="socials">
      <span></span><span></span><span></span>
      <span><svg width="12" height="9" viewBox="0 0 12 9"><rect x=".5" y=".5" width="11" height="8" fill="none" stroke="#5b5b5b"/><path d="M.5 .5L6 5L11.5 .5" fill="none" stroke="#5b5b5b"/></svg></span>
    </div>
    <div class="newsletter-label">Subscribe monthly Newsletter</div>
    <form class="newsletter"><input type="text" placeholder="Enter your email address"><button type="button">GO</button></form>
    <div class="col-rule" style="left:491px"></div>
    <h4 style="left:528px">CONTACT US</h4>
    <dl class="contact">
      <dt>Phone</dt><dd>(555) 010-2040</dd>
      <dt>Email</dt><dd>hello@tidyhavenco.example</dd>
      <dt>Address</dt><dd>1200 Example Ridge Road Suite 400<br>Springfield | New State | 00000</dd>
    </dl>
  </footer>
  <div class="copyright">Copyright © 2014 . All rights Reserved</div>
</div>
</body>
</html>
```